Amber Kite Foundation Inforgraphic

We are in need of an infographic layout to highlight facts for a medical foundation - the Amber Kite Foundation. We are a foundation dedicated to early detection and screening of pulmonary arterial hypertension, a deadly combination heart and lung disease We need a graphic that incorporates the following facts:

(1) Pulmonary Hypertension Symptoms: •Chest Pain
•Dizziness
•Shortness of Breath
•Fatigue
•Edema or swelling
•Cyanosis or skin discoloration

(2) Typically PH patients are consulted by 3 or more physicians before diagnosis

(3) PH patient’s generally incur 2.8 years between symptom onset and diagnosis via right heart catheterization

(4) Left untreated, the average life expectancy of a PAH patient is approximately 3 years from symptom onset

(5) No improvement has been achieved in early detection rates of PH since 1995

(6) 5 year survival rates are measured at 86% for PH patients diagnosed in early stages. 5 year survival rates for PH patients diagnosed late stages decrease to 50%

We want to incorporate these highlights into a fun and easy to follow infographic that can be transferred onto a large scale display banner.

We want to utilize our logo somewhere on the graphic. The logo file is attached. We also want to incorporate our slogan: Igniting the (ph)ight against pulmonary arterial hypertension through early detection and screening.

Thanks.

Industry/Entity Type

Medical

Colors
0555a3
3176b5
85acd3

Requirements
Must have
• Amber Kite Foundation Logo
• Dynamic display of graphics and figures to highlight statistics in the project discription

```html
<!DOCTYPE html>
<html lang="en">
<head>
<meta charset="utf-8">
<title>Amber Kite Foundation – Early Detection of Pulmonary Arterial Hypertension</title>
<link href="https://fonts.googleapis.com/css2?family=Bebas+Neue&family=Oswald:wght@500;600&family=Libre+Baskerville&display=swap" rel="stylesheet">
<style>
  :root {
    --navy: #0555a3;
    --mid: #3176b5;
    --light: #85acd3;
    --paper: #f3f1ea;
    --band-light: #7aa3d1;
    --band-mid: #3272b8;
    --band-deep: #2f6bb3;
    --box: #1f5fae;
    --footer: #0e2f6a;
    --ink-white: #ffffff;
    --numeral: #ecebe4;
    --slogan: #7fa6d6;
    --pointer: #b9e0c8;
  }
  * { margin: 0; padding: 0; box-sizing: border-box; }
  html, body { width: 1200px; height: 3600px; overflow: hidden; background: var(--paper); }
  .poster { position: relative; width: 1200px; height: 3600px; background: var(--paper); font-family: "Oswald", sans-serif; }

  .brand { position: absolute; top: 88px; left: 0; width: 1200px; text-align: center;
           font-family: "Oswald", sans-serif; font-weight: 500; font-size: 44px; letter-spacing: 6px; color: var(--navy); }
  .slogan { position: absolute; top: 196px; left: 0; width: 1200px; text-align: center;
            font-family: "Oswald", sans-serif; font-weight: 500; font-size: 21px; line-height: 26px; letter-spacing: 2px; color: var(--slogan); }

  .title-banner { position: absolute; top: 0; left: 0; width: 1200px; height: 720px; }
  .ribbon-text { position: absolute; top: 322px; left: 0; width: 1200px; text-align: center;
                 font-family: "Libre Baskerville", serif; font-size: 32px; letter-spacing: 4px; color: var(--ink-white); }
  .headline { position: absolute; left: 0; width: 1200px; text-align: center;
              font-family: "Bebas Neue", sans-serif; font-size: 132px; line-height: 1; letter-spacing: 1px; color: var(--ink-white); }
  .headline.line-1 { top: 418px; }
  .headline.line-2 { top: 556px; }

  .symptoms { position: absolute; top: 720px; left: 0; width: 1200px; height: 810px; }
  .numeral { position: absolute; font-family: "Bebas Neue", sans-serif; line-height: 1; }
  .symptoms .numeral { left: 100px; top: 128px; font-size: 220px; color: var(--light); }
  .symptoms-title { position: absolute; left: 232px; top: 108px; font-family: "Oswald", sans-serif; font-weight: 600;
                    font-size: 33px; line-height: 38px; letter-spacing: 1px; color: var(--navy); }
  .symptoms-title .accent { color: var(--light); }
  .symptom-chart { position: absolute; top: 0; left: 0; }

  .fact { position: absolute; left: 0; width: 1200px; }
  .fact .numeral { left: 84px; font-size: 210px; color: var(--numeral); }
  .fact-text { position: absolute; left: 206px; width: 940px; font-family: "Oswald", sans-serif; font-weight: 500;
               font-size: 41px; line-height: 57px; letter-spacing: 2px; color: var(--ink-white); text-transform: uppercase; }
  .fact-2 { top: 1530px; height: 291px; background: var(--band-light); }
  .fact-3 { top: 1851px; height: 333px; background: var(--band-mid); }
  .fact-4 { top: 2214px; height: 372px; background: var(--band-light); }
  .fact-5 { top: 2634px; height: 315px; background: var(--band-mid); }
  .fact-6 { top: 2991px; height: 453px; background: var(--band-deep); }

  .footer { position: absolute; top: 3465px; left: 0; width: 1200px; height: 135px; background: var(--footer);
            display: flex; align-items: center; justify-content: center; }
  .footer-brand { font-family: "Oswald", sans-serif; font-weight: 500; font-size: 22px; letter-spacing: 4px; color: var(--ink-white); }
</style>
</head>
<body>
<main class="poster">

  <div class="brand">AMBER KITE FOUNDATION</div>
  <p class="slogan">IGNITING THE (PH)IGHT AGAINST PULMONARY ARTERIAL HYPERTENSION<br>THROUGH EARLY DETECTION AND SCREENING.</p>

  <svg class="title-banner" viewBox="0 0 1200 720" aria-hidden="true">
    <polygon points="30,300 84,300 84,390 30,390 56,345" fill="var(--mid)"/>
    <polygon points="1170,300 1116,300 1116,390 1170,390 1144,345" fill="var(--mid)"/>
    <polygon points="84,390 84,408 56,390" fill="#143f7a"/>
    <polygon points="1116,390 1116,408 1144,390" fill="#143f7a"/>
    <rect x="84" y="264" width="1032" height="436" fill="var(--box)"/>
    <rect x="98" y="278" width="1004" height="408" fill="none" stroke="#6f9ad0" stroke-width="3"/>
    <rect x="56" y="300" width="1088" height="90" fill="var(--mid)"/>
    <rect x="56" y="300" width="1088" height="90" fill="none" stroke="#9cbde2" stroke-width="2"/>
  </svg>
  <div class="ribbon-text">EARLY DETECTION &amp; STREANNING OF</div>
  <div class="headline line-1">PULMONARY ARTERIAL</div>
  <div class="headline line-2">HYPERTENSION!</div>

  <section class="symptoms">
    <svg class="symptom-chart" width="1200" height="810" viewBox="0 720 1200 810">
      <defs>
        <path id="track-outer" d="M647.1,1500.1 A330,330 0 1 1 1045.8,1355"/>
        <path id="track-mid" d="M670.4,1436.2 A262,262 0 1 1 986.9,1321"/>
        <path id="track-inner" d="M692.3,1376.1 A198,198 0 1 1 931.5,1289"/>
      </defs>
      <use href="#track-outer" fill="none" stroke="var(--navy)" stroke-width="64"/>
      <use href="#track-mid" fill="none" stroke="var(--mid)" stroke-width="60"/>
      <use href="#track-inner" fill="none" stroke="var(--light)" stroke-width="56"/>
      <line x1="820" y1="1215" x2="1150" y2="1420" stroke="var(--pointer)" stroke-width="3"/>
      <rect x="660" y="1060" width="200" height="180" rx="60" fill="var(--navy)" role="img" aria-label="Lungs icon"/>

      <g font-family="Oswald, sans-serif" font-weight="500" font-size="24" letter-spacing="2" fill="#ffffff">
        <text dy="9"><textPath href="#track-outer" startOffset="2%">SHORTNESS OF BREATH</textPath></text>
        <text dy="9"><textPath href="#track-outer" startOffset="86%" text-anchor="end">CHEST PAIN</textPath></text>
        <text dy="9"><textPath href="#track-mid" startOffset="2%">EDEMA OR SWELLING</textPath></text>
        <text dy="9"><textPath href="#track-mid" startOffset="86%" text-anchor="end">DIZZINESS</textPath></text>
        <text dy="9"><textPath href="#track-inner" startOffset="2%">EDEMA OR SWELLING</textPath></text>
        <text dy="9"><textPath href="#track-inner" startOffset="86%" text-anchor="end">FATIGUE</textPath></text>
      </g>
    </svg>
    <div class="numeral">1</div>
    <h2 class="symptoms-title">PULMONARY<br>HYPERTENSION<br><span class="accent">SYMPTOMS:</span></h2>
  </section>

  <section class="fact fact-2">
    <div class="numeral" style="top:48px">2</div>
    <p class="fact-text" style="top:70px">Typically PH patients are consulted<br>by 3 or more physicians before<br>diagnosis</p>
  </section>

  <section class="fact fact-3">
    <div class="numeral" style="top:64px">3</div>
    <p class="fact-text" style="top:82px">PH patients generally incur 2.8 years<br>between symptom onset and diagnosis<br>via right heart catheterization</p>
  </section>

  <section class="fact fact-4">
    <div class="numeral" style="top:76px">4</div>
    <p class="fact-text" style="top:72px">Left untreated, the average life<br>expectancy of a PAH patient is<br>approximately 3 years from<br>symptom onset</p>
  </section>

  <section class="fact fact-5">
    <div class="numeral" style="top:52px">5</div>
    <p class="fact-text" style="top:70px">No improvement has been achieved<br>in early detection rates of<br>PH since 1995</p>
  </section>

  <section class="fact fact-6">
    <div class="numeral" style="top:96px">6</div>
    <p class="fact-text" style="top:72px">5 year survival rates are measured<br>at 86% for PH patients diagnosed in<br>early stages. 5 year survival rates<br>for PH patients diagnosed late stages<br>decrease to 50%</p>
  </section>

  <footer class="footer">
    <span class="footer-brand">AMBER KITE FOUNDATION</span>
  </footer>

</main>
</body>
</html>
```